Need a new office flyer

I would like an 8.5 x 11" flyer made that can be emailed or printed out and handed to potential customers.  The flyer should include our existing logo and continuity of branding.   I am a commercial real estate broker and market myself to business with 5-50 employee's that are looking to buy or lease space to run their business from.  I focus my efforts on office & warehouse space. The flyer should have a banner "need a new location "
"VLD commercial real estate specializes in helping business and professionals buy/sell or lease  the best spaces for their business.  Take the stress & time out of finding the best location for your business and negotiating a great deal  VLD will do it for you and the best part our service is free to you. Working with VLD is easy as 1, 2, 3
1. Call, Text, Email us today and let us know what your looking to do.
2. VLD  will prepare a list of all the best available spaces that meet your specifications and set up tours of your favorites.
3. We will negotiate the best terms for your space. and help you with all the  details of getting your new space ready for you.
Don't forget the that our services are free to Buyers and Tenants so don't waste your companies time searching for locations, we already know where they are!
Contact us today!
Dale Norcutt
DRE 07354128
VLD Commercial Real Estate
555-317-4829
d.norcutt@vldprop-example.com

```html
<!DOCTYPE html>
<html lang="en">
<head>
<meta charset="utf-8">
<title>VLD Commercial Real Estate – Need a New Location</title>
<link rel="stylesheet" href="https://fonts.googleapis.com/css2?family=Oswald:wght@600;700&family=Montserrat:wght@500;600;700;800&display=swap">
<style>
  :root{
    --brand-blue:#2f6da8;
    --brand-gray:#8e8e90;
    --panel-gray:#9a9a9c;
    --ink:#1d1d1f;
    --dark-bar:#2b2b2d;
    --paper:#ffffff;
    --backdrop:#e9e9eb;
  }
  *{box-sizing:border-box;margin:0;padding:0}
  html,body{width:1200px;height:800px;overflow:hidden;background:var(--backdrop)}
  .canvas{position:relative;width:1200px;height:800px}
  .flyer{position:absolute;left:300px;top:12px;width:600px;height:776px;background:var(--paper);overflow:hidden;box-shadow:0 4px 18px rgba(0,0,0,.15);font-family:"Montserrat",sans-serif;color:var(--ink)}
  .hero{position:absolute;left:0;top:0;width:600px;height:280px}
  .brand{position:absolute;left:34px;top:150px;display:flex;align-items:center;gap:10px}
  .brand-dot{width:40px;height:40px;border-radius:50%;border:4px solid var(--brand-blue)}
  .brand-name{font-weight:800;font-size:42px;line-height:1;color:var(--brand-blue);letter-spacing:1px}
  .brand-tag{position:absolute;left:86px;top:196px;font-size:7px;font-weight:600;letter-spacing:2.5px;color:var(--brand-gray)}
  .headline{position:absolute;left:34px;top:212px;font-family:"Oswald",sans-serif;font-weight:700;line-height:.95;text-transform:uppercase}
  .headline .line-1{display:block;font-size:36px;color:var(--brand-blue)}
  .headline .line-2{display:block;font-size:60px;color:var(--brand-gray)}
  .intro{position:absolute;left:34px;top:312px;width:340px;font-size:12px;font-weight:600;line-height:1.38}
  .step{position:absolute;color:#fff;font-size:11px;font-weight:600;line-height:1.38;text-align:center;padding:34px 14px 12px}
  .step-1{left:34px;top:526px;width:178px;background:var(--panel-gray)}
  .step-2{left:212px;top:464px;width:178px;background:var(--brand-blue)}
  .step-3{left:390px;top:390px;width:176px;background:var(--panel-gray)}
  .step-num{position:absolute;left:50%;top:-26px;transform:translateX(-50%);width:52px;height:52px;border-radius:50%;background:#fff;border:4px solid var(--brand-blue);font-family:"Oswald",sans-serif;font-weight:700;font-size:30px;line-height:44px;color:var(--brand-blue);text-align:center}
  .portrait-ring{position:absolute;left:432px;top:536px;width:120px;height:120px;border-radius:50%;border:5px solid var(--brand-blue);background:#fff;padding:5px}
  .portrait{width:100%;height:100%;border-radius:50%;background:radial-gradient(circle at 50% 40%,#b9b4ae,#5d5d60 70%,#2e2e32)}
  .closing{position:absolute;left:34px;top:630px;width:370px;font-size:12px;font-weight:600;line-height:1.38}
  .agent{position:absolute;right:40px;top:662px;text-align:right;line-height:1.2}
  .agent-name{font-family:"Oswald",sans-serif;font-weight:700;font-size:17px}
  .agent-title{font-size:11px;font-weight:700;color:var(--brand-blue)}
  .agent-license{font-size:9px;font-weight:500}
  .cta{position:absolute;left:34px;top:686px;padding:2px 22px 2px 14px;background:var(--brand-blue);color:#fff;border-radius:0 14px 14px 0;font-family:"Oswald",sans-serif;font-weight:700;font-size:16px;line-height:24px;text-transform:uppercase}
  .company{position:absolute;left:34px;top:715px;font-size:12px;font-weight:800;line-height:16px}
  .contact-bar{position:absolute;left:0;bottom:0;width:600px;height:40px;background:var(--dark-bar);color:#fff;display:flex;align-items:center;gap:20px;padding-left:34px;font-size:14px;font-weight:600}
  .contact-item{display:flex;align-items:center;gap:8px}
  .contact-item svg{width:18px;height:18px}
  .divider{width:1px;height:22px;background:#777}
</style>
</head>
<body>
<div class="canvas">
  <article class="flyer">
    <svg class="hero" viewBox="0 0 600 280">
      <defs>
        <linearGradient id="skyline" x1="0" y1="0" x2="1" y2="1">
          <stop offset="0" stop-color="#c9d6e8"/>
          <stop offset=".45" stop-color="#5f84b4"/>
          <stop offset="1" stop-color="#1e3556"/>
        </linearGradient>
      </defs>
      <circle cx="440" cy="60" r="192" fill="none" stroke="var(--brand-blue)" stroke-width="11"/>
      <circle cx="440" cy="60" r="179" fill="none" stroke="#b4b4b6" stroke-width="7" stroke-dasharray="200 1200" stroke-dashoffset="-120"/>
      <circle cx="440" cy="60" r="172" fill="url(#skyline)" role="img" aria-label="Photo looking up at glass office towers against the sky"/>
    </svg>

    <div class="brand"><span class="brand-dot"></span><span class="brand-name">VLD</span></div>
    <div class="brand-tag">COMMERCIAL REAL ESTATE</div>

    <h1 class="headline"><span class="line-1">Need a new</span><span class="line-2">Location</span></h1>

    <p class="intro">VLD commercial real estate specializes in helping business and professionals buy/sell or lease the best spaces for their business. Take the stress &amp; time out of finding the best location for your business and negotiating a great deal VLD will do it for you and the best part our service is free to you.</p>

    <div class="step step-3"><span class="step-num">3</span>We will negotiate the best terms for your space. and help you with all the details of getting your new space ready for you.</div>
    <div class="step step-2"><span class="step-num">2</span>VLD will prepare a list of all the best available spaces that meet your specifications and set up tours of your favorites.</div>
    <div class="step step-1"><span class="step-num">1</span>Call, Text, Email us today and let us know what your looking to do.</div>

    <div class="portrait-ring"><div class="portrait" role="img" aria-label="Portrait photo of Dale Norcutt"></div></div>

    <p class="closing">Don't forget the that our services are free to Buyers and Tenants so don't waste your companies time searching for locations, we already know where they are!</p>

    <div class="agent">
      <div class="agent-name">Dale Norcutt</div>
      <div class="agent-title">Managing Director</div>
      <div class="agent-license">DRE # 07354128</div>
    </div>

    <div class="cta">Contact us today!</div>
    <div class="company">VLD Commercial Real Estate</div>

    <footer class="contact-bar">
      <span class="contact-item">
        <svg viewBox="0 0 20 20"><circle cx="10" cy="10" r="9" fill="#8e8e90"/><path d="M6.5 5.5l2 .3.6 2.2-1.2.9a7 7 0 0 0 3.2 3.2l.9-1.2 2.2.6.3 2-1.2 1A9 9 0 0 1 5.5 6.7z" fill="#2b2b2d"/></svg>
        555-317-4829
      </span>
      <span class="divider"></span>
      <span class="contact-item">
        <svg viewBox="0 0 20 20"><circle cx="10" cy="10" r="9" fill="#8e8e90"/><rect x="5" y="6.5" width="10" height="7" fill="#2b2b2d"/><path d="M5 6.5l5 4 5-4" fill="none" stroke="#8e8e90" stroke-width="1"/></svg>
        d.norcutt@vldprop-example.com
      </span>
    </footer>
  </article>
</div>
</body>
</html>
```